Briefpapier für Betrieb aus der Landwirtschaft
Zielgruppe
der Firmen name ist Brandol Jürgen
Wir sind ein Betrieb der aus der Landwirtschaft kommt und sich auf die bewirtschaftung von Streuobstäckern und wiesen spezialisiert hat.
Die Früchte der Bäume werden über eine von uns mitgegründete Genossenschaft vertrieben... Andere Früchte werden an destilierien und an Endverbraucher verkauft.
Zielgruppe:
Das Breifpapier soll für geschäftsbriefe rechnungen Lieferscheine, auftragsbestätigungen verwendung finden.
Und an Endkunden, Lieferanten und Geschaftspartner gehen !!
Wir haben ein Biolabel gegründet wiesel pur terra eventuell kann man sich an dem Logo orientieren !!
Aufgabenstellung
Ich habe unseren alten Briefbogen angehängt !!! Bitte nicht kopieren oder optimieren !!! Er ist nur da um die Daten zu nehmen !!! Briefpapier soll kompl. neu desingt werden... Firmen Name Brandol Jürgen
Ich brauche platz für die Biosiegel 2 in der Zahl
Frech / Modern eventuell mit wasserzeichen , hohen wiedererkennungswert.
Nach abschluss des desingns sollen Visitenkarten gemacht werden

```html
<!DOCTYPE html>
<html lang="de">
<head>
<meta charset="utf-8">
<title>Briefpapier Brandol Jürgen</title>
<link href="https://fonts.googleapis.com/css2?family=Montserrat:wght@400;500;600;700&family=Arimo:wght@400;700&display=swap" rel="stylesheet">
<style>
  :root{
    --stage:#9c9c9c;
    --paper:#ffffff;
    --lime:#95c11f;
    --forest:#126b32;
    --panel:#d9e6b3;
    --ink:#2b2b2b;
    --logo-ink:#555555;
    --panel-ink:#3a3a3a;
  }
  *{box-sizing:border-box;margin:0;padding:0}
  html,body{width:1200px;height:720px;overflow:hidden}
  body{background:var(--stage);position:relative;font-family:"Arimo",Arial,sans-serif}
  .sheet{position:absolute;top:49px;width:428px;height:605px;background:var(--paper);overflow:hidden}
  .sheet--blank{left:113px}
  .sheet--letter{left:668px}
  .sheet__art{position:absolute;inset:0;width:428px;height:605px}
  .brand{position:absolute;left:48px;top:45px;display:flex;align-items:center;gap:6px;
    font-family:"Montserrat",sans-serif;font-weight:500;font-size:16px;letter-spacing:.2px;color:var(--logo-ink)}
  .brand__dot{width:19px;height:19px;border-radius:50%;background:var(--lime)}
  .sender-line{position:absolute;left:48px;top:97px;font-family:"Montserrat",sans-serif;font-size:3.6px;color:#666}
  .contact-panel{position:absolute;left:309px;top:0;width:103px;height:221px}
  .contact-panel__body{position:absolute;left:0;top:0;width:100px;height:216px;background:var(--panel);
    border-radius:0 0 14px 14px;padding:49px 0 0 10px;font-family:"Montserrat",sans-serif;color:var(--panel-ink);
    font-size:5px;line-height:6px}
  .contact-panel__label{font-size:3.6px;text-transform:uppercase;letter-spacing:.2px;color:#555;line-height:5px}
  .contact-panel__group{margin-bottom:4px}
  .contact-panel__group--wide{margin-bottom:8px}
  .recipient{position:absolute;left:48px;top:112px;font-size:7.6px;line-height:8.7px;color:var(--ink)}
  .subject{position:absolute;left:48px;top:233px;font-size:7.6px;font-weight:700;color:var(--ink)}
  .salutation{position:absolute;left:48px;top:262px;font-size:7.6px;color:var(--ink)}
  .letter-body{position:absolute;left:48px;top:280px;width:326px;font-size:7.5px;line-height:9.5px;
    color:var(--ink);text-align:justify;hyphens:auto}
  .seal-name{position:absolute;left:226px;top:563px;display:flex;align-items:center;gap:5px;
    font-family:"Montserrat",sans-serif;font-weight:600;font-size:11px;line-height:11.5px;color:#fff}
  .seal-name__dot{width:14px;height:14px;border-radius:50%;background:#fff}
  .partner-badge{position:absolute;left:354px;top:549px;width:40px;height:40px;background:#fff}
  .stage-band{position:absolute;left:0;bottom:0;width:1200px;height:22px;background:var(--lime);border-top:6px solid #fff}
</style>
</head>
<body>

<svg width="0" height="0" style="position:absolute">
  <defs>
    <linearGradient id="wave-fill" x1="0" y1="0" x2="1" y2="0">
      <stop offset="0" stop-color="#95c11f"/>
      <stop offset="0.45" stop-color="#6aa22a"/>
      <stop offset="1" stop-color="#126b32"/>
    </linearGradient>
    <linearGradient id="strip-fill" x1="0" y1="0" x2="0" y2="1">
      <stop offset="0" stop-color="#95c11f"/>
      <stop offset="1" stop-color="#126b32"/>
    </linearGradient>
  </defs>
</svg>

<!-- blank letterhead -->
<section class="sheet sheet--blank">
  <svg class="sheet__art" viewBox="0 0 428 605" aria-hidden="true">
    <path d="M0 0 H67 C30 18 8 48 0 82 Z" fill="#95c11f"/>
    <path d="M309 0 H412 V255 Z" fill="none"/>
    <path d="M312 0 H412 V206 Q412 221 397 221 H326 Q312 221 312 210 Z" fill="#126b32"/>
    <rect x="408" y="0" width="4" height="206" fill="url(#strip-fill)"/>
    <path d="M41 605 C90 575 130 560 168 555 C230 545 300 530 347 509 C395 488 420 465 428 444 L428 605 Z" fill="url(#wave-fill)"/>
  </svg>
  <div class="brand"><span class="brand__dot"></span>BRANDOL JÜRGEN</div>
  <p class="sender-line">Jürgen Brandol . Lindenweg 12 . 97321 Obernau OT Hasenfeld</p>
  <aside class="contact-panel">
    <div class="contact-panel__body">
      <div class="contact-panel__group"><p class="contact-panel__label">Verantwortlicher</p><p>Jürgen Brandol<br>Geschäftsführer</p></div>
      <div class="contact-panel__group"><p class="contact-panel__label">Kontaktdaten</p><p>Lindenweg 12<br>97321 Obernau<br>OT Hasenfeld</p></div>
      <div class="contact-panel__group"><p>Fon +49 (0)9351 4407312<br>Fax +49 (0)9351 440731</p></div>
      <div class="contact-panel__group--wide"><p>kontakt@juergenbrandol.de<br>www.juergenbrandol.de</p></div>
      <div class="contact-panel__group--wide"><p class="contact-panel__label">Steuernummer</p><p>218/365/40912</p></div>
      <div class="contact-panel__group"><p class="contact-panel__label">Bankverbindung</p><p>Nordtal Bank<br>IBAN DE17600502037730119546<br>BIC&nbsp;&nbsp; NOTADEFFXXX</p></div>
      <div><p>Kto.-Nr. 7730119546<br>BLZ&nbsp;&nbsp;&nbsp;&nbsp;&nbsp;&nbsp; 600 502 03</p></div>
    </div>
  </aside>
  <div class="seal-name"><span>WIESEL PUR<br>TERRA</span><span class="seal-name__dot"></span></div>
  <div class="partner-badge" role="img" aria-label="Platz für Biosiegel"></div>
</section>

<!-- filled letter -->
<section class="sheet sheet--letter">
  <svg class="sheet__art" viewBox="0 0 428 605" aria-hidden="true">
    <path d="M0 0 H67 C30 18 8 48 0 82 Z" fill="#95c11f"/>
    <path d="M312 0 H412 V206 Q412 221 397 221 H326 Q312 221 312 210 Z" fill="#126b32"/>
    <rect x="408" y="0" width="4" height="206" fill="url(#strip-fill)"/>
    <path d="M41 605 C90 575 130 560 168 555 C230 545 300 530 347 509 C395 488 420 465 428 444 L428 605 Z" fill="url(#wave-fill)"/>
  </svg>
  <div class="brand"><span class="brand__dot"></span>BRANDOL JÜRGEN</div>
  <p class="sender-line">Jürgen Brandol . Lindenweg 12 . 97321 Obernau OT Hasenfeld</p>
  <aside class="contact-panel">
    <div class="contact-panel__body">
      <div class="contact-panel__group"><p class="contact-panel__label">Verantwortlicher</p><p>Jürgen Brandol<br>Geschäftsführer</p></div>
      <div class="contact-panel__group"><p class="contact-panel__label">Kontaktdaten</p><p>Lindenweg 12<br>97321 Obernau<br>OT Hasenfeld</p></div>
      <div class="contact-panel__group"><p>Fon +49 (0)9351 4407312<br>Fax +49 (0)9351 440731</p></div>
      <div class="contact-panel__group--wide"><p>kontakt@juergenbrandol.de<br>www.juergenbrandol.de</p></div>
      <div class="contact-panel__group--wide"><p class="contact-panel__label">Steuernummer</p><p>218/365/40912</p></div>
      <div class="contact-panel__group"><p class="contact-panel__label">Bankverbindung</p><p>Nordtal Bank<br>IBAN DE17600502037730119546<br>BIC&nbsp;&nbsp; NOTADEFFXXX</p></div>
      <div><p>Kto.-Nr. 7730119546<br>BLZ&nbsp;&nbsp;&nbsp;&nbsp;&nbsp;&nbsp; 600 502 03</p></div>
    </div>
  </aside>
  <address class="recipient" style="font-style:normal">Firma<br>Herrn Max Mustermann<br>Straße Hausnummer<br>PLZ Ort</address>
  <p class="subject">Betreffszeile</p>
  <p class="salutation">Sehr geehrter Herr Mustermann,</p>
  <div class="letter-body">
    <p>Iciuntur minctat reritas inctotae cusa quam, ut hillatemo incti simus sum ipiciliquia simi, nus quam aditatur mollitiatur?</p>
    <p>Ihit evenihillam, venimi, sumquid itaturiae plat quis con nis nem es volo que net pos nusci cum voluptur archilligent labor sumqui represtemo cum fugitat ibuscimusam erferum se natur?</p>
    <p>Ovitas ut porendigente nullabore, et mod eni te enest liciis quam si sunt, sam, cum ullias millorrumque dollatet que venda et ut volores erspici enduscias ma pos ut quiditiam ape nos doluptatur sae de aut essi digenis aut quodicia aut facestia quaepe sum volore net fugita culpa quae nis reperum quo mos num es dio. Et magnist volorerupis es atatem int assit quam rempele ssimoluptio velit, qui cum rate dolore ducipsa nisqui consed modit libus, totat parum, ius et eatem labo. Neque acea quassequi dolestr uptatist, si as quassit ectotatis dolor suntem re sinctiur? Oreperferae. Et arcidusda nia nam lantur am ipient voluptaquam volorio maxim quatatur, te non rest et qui id et occati nonsecea volorposant.</p>
    <p>Aximill estemque eos nonsentint apitem. Unda aliatus dignitatem la voluptat.</p>
    <p>Nemolum as ea dolorest fugia venes comnitam, totae. Tatur assequae consequiae ex elenihil modis a comnim duciend untibus, atende illabo. Fugianto culparc hillorp orerspe rsperibus maximin istentiatis endist, utatatur?</p>
    <p>Aximodio. Itates auditibus, iducima quis alit eaque venist quatque plaborem autatio mi, quod quatumquatur sita cumqui te ne nos apicit explignis sitam, nostrum eatia vel etum, sam reriam eiur antem quod qui que voluptatem rat porerias dolore iliaturio officab oratiae rem. Ad que nulloreiunt.</p>
    <p>Hendit, expel mi, sit lacest ella voluptas dolorer ciligent lab ium quo quaecaborem quis sequamus.</p>
    <p>Iciam, voluptam harunte mposandam aperchil ius.</p>
    <p>Nat. Nobis volorrores idis duci doluptae asint.</p>
  </div>
  <div class="seal-name"><span>WIESEL PUR<br>TERRA</span><span class="seal-name__dot"></span></div>
  <div class="partner-badge" role="img" aria-label="Platz für Biosiegel"></div>
</section>

<div class="stage-band"></div>
</body>
</html>
```